Major Australian Food and Wine Event Web Design Project

The project will consist of 3 designs
The homepage
A city hub page
A general content page

The main audience who will visit the website will be (in Order of importance:

1) Visitors
- Mainly women 24 – 54 years (they are the main ticket buyers)
- In a relationship – so will go to the show with their partner
- In a good paying job or home maker – and who have disposable income to spend $30 a ticker
- Enjoy food, wine and going out
- Looking for a fun day out – although an event that is about food and wine – it is an event that most people will go to and have a fun day out – not too pretentious

A smaller proportion of the audience will be:
2) Exhibitors & sponsors ( both prospective and existing)
3) Media

Objectives:

- Functionality on home page and sub pages needs to be updated, clear, easy to navigate and inject a sense of ‘fun’ – need to make it look more professional
- Need to incorporate the many things that need to be on the home page and sub pages in a visually appealing manner
- Ensure the ‘Cons’ above are considered and reflected in functionality and design
- To not be too focus on the colours (these can be changed) – but focus on the functionality and overall design opportunities.

Approach:

Keywords to describe the Bright Plate & Vine Fair:
Fun day out, discover, learn, indulge, entertaining

Other website examples:

Some great consumers event websites from the UK really make our website look basic and juvenile – and below are some examples of the presentation of how we would like our website to look like:

http://www.morselfairs-example.com/london/ This website is clean, includes good social media integration and exudes a sense of fun. Their content pages, such as the features landing page also presents options in a clear and visually appealing way with a series of boxes including image and text http://www.morselfairs-example.com/london/content/343/Features

http://www.homecraftexpo-example.com/ - this is also a great website – and it incorporates all the elements we would be looking for on our homepage – but the background/skin also includes a sense of fun and cheekiness. Subpages also are consistent.

Features

• Its a fun day that offers great value for money
• Caters to all visitors, regardless of different levels of knowledge or interest in food, wine and cooking.
• Sample great quality food and wine products from hundreds of reputable exhibitors
• Learn more through many of the shows feature activities (Celeb Theatre, Wine Theatre, Cooking & Cheese Classes)

Functionality & Structure:

In a user friendly, easy to view way, we need to incorporate the following functionality elements on home page:
- main header (that will incorporate our current creative) with a ‘fun’ skin
- navigation tabs/references (hone, location, tickets, blog, sign up, exhibitors)
- navigation/content banner (rotating)
- Area for small intro about the show
- News and highlight section
- New exhibitors section
- Obvious Ticket call to action
- Obvious sign up call to action
- Social media buttons or links ( really like the moving gifs on the Homecraftexpo-example.com site
- area for advertising (MREC size) to sell to exhibitors/sponsors
- Show dates for all 5 shows (maybe in main header)

Subpage layout is also important and needs to reflect the homepage – so would also like to see examples of how this would look and tie in with navigation – we generally have a lot of content on these pages, so clear navigation would be useful. – see below for further details of functionality for city Hubs

‘CITY HUB’ BRIEF
When navigating to each location the user will be taken to a ‘CITY HUB’ which should replicate design and content elements of a main HOME page, as well as reflect more specific information for each Show. Elements which must appear on this page are:
• FEATURES – which may be displayed in categories (in boxes, see appendix 1.0) which will link through to relevant content pages. Or in one box which will link through to a features page with all presented in boxes
• CHEFS – may be displayed as a separate icon box which will link to chefs page with bios, Celeb Theatre timetable etc.
• TICKETS – either a button or clear callout to purchase tickets
• PLAN YOUR DAY – may be displayed in a separate content box which will then link through to getting there, sample itineraries and downloadable pocket show guide for visitors to print before coming to the Show.
• WHO’S EXHIBITING – to link back to city specific exhibitor lists

Our current website is out of date and has the following inadequacies (www.brightplatefair-example.com.au) -

The homepage
A city hub page
A general content page

1) Visitors

3) Media

Objectives:

Approach:

To be perceived as a fun, entertaining event with something for everyone - website creative and navigation must reflect this.

Other website examples:

Features

- New exhibitors section

‘CITY HUB’ BRIEF

- Dated design/layout
- Homepage too text heavy
- No content boxes that can be used for different features/areas (eg. News, Exhibitors etc)
- Uninspiring colours and skin(eg. grey background), does not reflect ‘a fun day out’
- Limited presence of social media platforms and lacks ‘community’
- No continuity in sub pages
- main banner too big – takes up too much space on homepage

Requirements
Must have
• As per above brief.

In addition:
Floating social media buttons on side
Wrap around image
Drop down menu (specifically for the location nav item)

```html
<!DOCTYPE html>
<html lang="en">
<head>
<meta charset="utf-8">
<title>Bright Plate &amp; Vine Fair</title>
<link rel="stylesheet" href="https://fonts.googleapis.com/css2?family=Arimo:wght@400;700&family=Libre+Baskerville&display=swap">
<style>
:root{
  --peach:#fde0c6;
  --white:#ffffff;
  --orange:#f26a1b;
  --orange-light:#ffb47a;
  --maroon:#9a2c14;
  --ink:#222222;
  --text:#333333;
  --muted:#8a8a8a;
  --rule:#d6d6d6;
  --hero-grey:#d9d9d9;
}
*{box-sizing:border-box;margin:0;padding:0}
html,body{width:1044px;height:1200px;overflow:hidden}
body{position:relative;background:var(--peach);font-family:"Arimo",Arial,sans-serif;color:var(--text)}
a{color:inherit;text-decoration:none}
.abs{position:absolute}

.top-band{left:0;top:0;width:1044px;height:108px;background:var(--white)}
.brand-box{left:53px;top:0;width:196px;height:143px;background:var(--white);border-radius:0 0 22px 22px;box-shadow:0 2px 6px rgba(0,0,0,.18);display:flex;align-items:center;justify-content:center;text-align:center;padding:0 18px}
.brand-name{font-size:25px;line-height:1.1;color:var(--ink);font-weight:700}
.utility-links{right:80px;top:9px;font-size:10px;color:var(--muted);letter-spacing:.3px}
.utility-links span{margin:0 6px}
.exhibitor-btn{left:848px;top:45px;width:121px;height:23px;border-radius:12px;background:linear-gradient(#ff9a5c,#f2621a);color:#fff;font-size:10px;display:flex;align-items:center;justify-content:center;box-shadow:0 1px 2px rgba(0,0,0,.25)}

.nav-marker{left:411px;top:87px;width:30px;height:30px;border-radius:50%;background:radial-gradient(circle at 50% 55%,#e5401a 40%,#f6c7a0 42%)}
.main-nav a{position:absolute;top:119px;font-size:15px;color:var(--ink);letter-spacing:.4px}
.main-nav a.current{color:var(--orange)}

.content-panel{left:46px;top:158px;width:940px;height:724px;background:var(--white);border-radius:10px}
.hero{left:59px;top:172px;width:643px;height:305px;border-radius:14px;overflow:hidden;background:linear-gradient(180deg,#f4f4f4 0%,#d3d3d3 70%,#b9b9b9 100%)}
.hero-photo{position:absolute;left:200px;top:30px;width:380px;height:275px;background:linear-gradient(180deg,#e8e8e8,#9a9a9a 60%,#e7b43a 88%)}
.hero-line{position:absolute;font-family:"Libre Baskerville",Georgia,serif;font-size:21px;line-height:33.5px;color:#444;letter-spacing:.5px;text-transform:uppercase}
.hero-line.left{left:14px;top:28px}
.hero-line.right{right:24px;top:22px;text-align:right}

.events-card{left:720px;top:145px;width:250px;height:253px;border-radius:8px 8px 18px 18px;background:linear-gradient(180deg,#fff3ea 0%,#ffd3ae 45%,#fb9a4f 80%,#f58227 100%);box-shadow:0 3px 6px rgba(0,0,0,.2);padding:28px 20px 0 22px}
.events-card h2{font-weight:400;font-size:18px;color:var(--ink);margin-bottom:14px;letter-spacing:.3px}
.event-row{display:flex;height:33px;align-items:center;font-size:13px;color:var(--ink);border-bottom:1px solid rgba(255,255,255,.8);letter-spacing:.3px}
.event-row:last-child{border-bottom:0}
.event-row .city{width:104px}

.social-rail{left:986px;top:238px;width:50px;height:158px;background:var(--white);box-shadow:0 1px 4px rgba(0,0,0,.2);padding-top:12px}
.social-rail span{display:block;width:17px;height:17px;margin:0 auto 14px;border-radius:3px;background:#7d97b8}

.newsletter-label{left:738px;top:431px;font-size:14px;color:var(--ink);letter-spacing:.4px}
.newsletter-box{left:719px;top:457px;width:250px;height:63px;border-radius:10px;background:linear-gradient(#f7f7f7,#d8d8d8);border:1px solid #cfcfcf}
.email-field{position:absolute;left:14px;top:19px;width:188px;height:26px;background:#fff;border:1px solid #bbb;font-size:14px;color:#666;padding:4px 6px;letter-spacing:.4px}
.go-label{position:absolute;left:210px;top:22px;font-size:18px;font-weight:700;color:#f08a33}
.tickets-btn{left:719px;top:543px;width:249px;height:43px;border-radius:10px;background:linear-gradient(#fff0e3,#ffa36a 55%,#f7641c);box-shadow:0 2px 3px rgba(0,0,0,.25);font-size:19px;font-weight:700;color:#5a3320;display:flex;align-items:center;justify-content:center;letter-spacing:.8px}
.ad-slot{left:719px;top:631px;width:237px;height:234px;background:linear-gradient(160deg,#e8eef5 0%,#f7f7f7 55%,#e9dede 80%,#c9231f 100%)}

.intro-title{left:64px;top:495px;font-size:16.5px;color:var(--maroon);letter-spacing:.3px}
.intro-copy{left:64px;top:519px;width:636px;font-size:11.6px;line-height:19.3px;text-align:justify;color:var(--ink);letter-spacing:.1px}
.more-link{font-size:10.5px;color:var(--orange);letter-spacing:.6px}

.section-title{font-size:15.5px;letter-spacing:.4px}
.section-title .accent{color:var(--maroon)}
.news-list,.exhibitor-list{font-size:12.4px;line-height:16.5px;color:#444;letter-spacing:.6px;text-align:justify}
.news-list b,.exhibitor-list b{color:#333}
.news-item{position:absolute;left:0;width:296px}
.news-rule{position:absolute;left:0;width:296px;border-top:1px dashed #aaa}
.ex-item{position:absolute;left:0;width:294px}
.ex-rule{position:absolute;left:0;width:294px;border-top:1px solid var(--rule)}

.partner-strip{left:46px;top:895px;width:940px;height:63px;background:var(--white);border-radius:10px;overflow:hidden}
.partner{position:absolute;top:22px;font-size:13px;font-weight:700;color:var(--ink)}
.partner-badge{position:absolute;left:330px;top:10px;width:48px;height:48px;border-radius:50%;border:1.5px solid #666}
.food-disc{position:absolute;top:16px;width:78px;height:78px;border-radius:50%;border:4px solid #e4e4e4}

.footer-col{top:990px;font-size:12px;line-height:19.2px;color:#4a3a30;letter-spacing:.3px}
.footer-col h3{font-size:12px;font-weight:700;color:var(--orange);margin-bottom:0}
.footer-divider{top:995px;width:1px;height:160px;background:#fff}
.organiser-badge{left:786px;top:1082px;width:115px;height:28px;background:#c41a12}
.organiser-text{left:785px;top:1117px;font-size:9.5px;line-height:19px;color:#333;letter-spacing:.2px}
</style>
</head>
<body>

<header>
  <div class="abs top-band"></div>
  <div class="abs brand-box"><span class="brand-name">Bright Plate &amp; Vine Fair</span></div>
  <nav class="abs utility-links"><a href="#">contact us</a><span>|</span><a href="#">news &amp; media releases</a><span>|</span><a href="#">sponsors</a></nav>
  <a class="abs exhibitor-btn" href="#">Exhibitor Information</a>
  <div class="abs nav-marker" role="img" aria-label="Small tomato marking the active menu item"></div>
  <nav class="main-nav">
    <a class="current" href="#" style="left:404px">Home</a>
    <a href="#" style="left:494px">Location</a>
    <a href="#" style="left:604px">Tickets</a>
    <a href="#" style="left:704px">Blog</a>
    <a href="#" style="left:785px">Exhibitors</a>
    <a href="#" style="left:906px">Sign up</a>
  </nav>
</header>

<main>
  <div class="abs content-panel"></div>

  <section class="abs hero">
    <div class="hero-photo" role="img" aria-label="Photo of four celebrity chefs standing behind a plated dish with a yellow ribbon"></div>
    <p class="hero-line left">Be inspired by<br>our celebrity<br>chefs live<br>on stage</p>
    <p class="hero-line right">Succumb<br>to your<br>senses</p>
  </section>

  <aside class="abs events-card">
    <h2>Events</h2>
    <div class="event-row"><span class="city">Melbourne</span><span>Jun 1-3, 2012</span></div>
    <div class="event-row"><span class="city">Sydney</span><span>Jun 22-24, 2012</span></div>
    <div class="event-row"><span class="city">Perth</span><span>Jul 13-15, 2012</span></div>
    <div class="event-row"><span class="city">Adelaide</span><span>Oct 12-14, 2012</span></div>
    <div class="event-row"><span class="city">Brisbane</span><span>Nov 9-11, 2012</span></div>
  </aside>

  <nav class="abs social-rail" aria-label="Social links">
    <span></span><span></span><span></span><span></span><span></span>
  </nav>

  <p class="abs newsletter-label">Sign up for Newsletter</p>
  <div class="abs newsletter-box">
    <div class="email-field">Email Id</div>
    <span class="go-label">Go</span>
  </div>
  <a class="abs tickets-btn" href="#">Get Tickets</a>
  <div class="abs ad-slot" role="img" aria-label="Advertising banner for a free web hosting service with a server graphic"></div>

  <h1 class="abs intro-title" style="font-weight:400">What is the Bright Plate &amp; Vine Fair?</h1>
  <p class="abs intro-copy">If you are looking for a great day out with friends, then dont miss the Bright Plate &amp; Vine Fair! Along with seeing a celebrity chef live on stage, you can also taste your way around the event and discover delicious food and wine products from a host of regional producers and exciting exhibitors. Education is another key component of the Bright Plate &amp; Vine Fair with premium wine appreciation classes, cheese and wine classes and many other exciting features that are sure to get your taste buds flaring!</p>
  <a class="abs more-link" href="#" style="left:641px;top:610px">Read More</a>

  <section>
    <h2 class="abs section-title" style="left:64px;top:640px;font-weight:400;color:var(--ink)">News <span class="accent">| Heighlights</span></h2>
    <div class="abs news-list" style="left:65px;top:671px;width:296px;height:190px">
      <p class="news-item" style="top:0"><b>Lorem Ipsum</b> is simply dummy text of the printing and typesetting industry. Lorem Ipsum has been the industry's standard</p>
      <div class="news-rule" style="top:59px"></div>
      <p class="news-item" style="top:70px"><b>Lorem Ipsum</b> is simply dummy text of the printing and typesetting industry. Lorem Ipsum has been the industry's standard</p>
      <div class="news-rule" style="top:128px"></div>
      <p class="news-item" style="top:137px"><b>Lorem Ipsum</b> is simply dummy text of the printing and typesetting industry. Lorem Ipsum has been the industry's standard</p>
    </div>
    <a class="abs more-link" href="#" style="left:304px;top:860px">view More</a>
  </section>

  <section>
    <h2 class="abs section-title" style="left:404px;top:640px;font-weight:400"><span class="accent">Exihibitors</span></h2>
    <div class="abs exhibitor-list" style="left:404px;top:676px;width:294px;height:170px">
      <p class="ex-item" style="top:0"><b>Lorem Ipsum</b> is simply dummy text of the printing and typesetting industry.</p>
      <div class="ex-rule" style="top:51px"></div>
      <p class="ex-item" style="top:70px"><b>Lorem Ipsum</b> is simply dummy text of the printing and typesetting industry.</p>
      <div class="ex-rule" style="top:122px"></div>
      <p class="ex-item" style="top:133px"><b>Lorem Ipsum</b> is simply dummy text of the printing and typesetting industry.</p>
    </div>
    <a class="abs more-link" href="#" style="left:645px;top:860px">view More</a>
  </section>

  <section class="abs partner-strip" aria-label="Partners">
    <span class="partner" style="left:28px">Coldwell&amp;Pike</span>
    <span class="partner" style="left:172px">Vessara</span>
    <span class="partner-badge"></span>
    <div class="food-disc" role="img" aria-label="Tomato" style="left:602px;background:#e0421c"></div>
    <div class="food-disc" role="img" aria-label="Pan of stir-fried food" style="left:672px;background:#3a3a36"></div>
    <div class="food-disc" role="img" aria-label="Plate of sushi" style="left:750px;background:#d9c9b3"></div>
    <div class="food-disc" role="img" aria-label="Sliced lime" style="left:826px;background:#b9c38a"></div>
  </section>
</main>

<footer>
  <div class="abs footer-col" style="left:75px">
    <h3>Bright Plate &amp; Vine Fair</h3>
    Home<br>Melbourne<br>Sydney<br>Perth<br>Adelaide<br>Brisbane<br>Want to Exhibit?<br>Recipe Club
  </div>
  <div class="abs footer-divider" style="left:286px"></div>
  <div class="abs footer-col" style="left:302px">
    <h3>Show Attractions</h3>
    Celebrity Theatre<br>Cheese Masterclass<br>Cooking School<br>Decanter Bar<br>Restaurant<br>Wine Theatre<br>Exhibitor list<br>Floor plans
  </div>
  <div class="abs footer-divider" style="left:533px"></div>
  <div class="abs footer-col" style="left:547px">
    <h3>Chef Bio's</h3>
    Clara Hensley<br>Owen Talbrook<br>Niko Varelas<br>Luc Dumarais<br>Ben Harlowe<br>Toby Wrenfield<br>Recipe Club<br>Login
  </div>
  <div class="abs footer-divider" style="left:772px"></div>
  <div class="abs organiser-badge"></div>
  <p class="abs organiser-text">Event organised by<br>Meridian Expos Australia.© 2012<br>Competition Terms &amp; Conditions</p>
</footer>

</body>
</html>
```